Business Card Design

we need a bussiness card for the transport company called Harvel Transport
name of contact person that should display on card is Mankirat Sekhon contact no 0478162093
we do the dry goods and frozen deliveries in melbourne every day
happy to beat any quote

Business

Contact Information for Business Card

Harvel transport
Mankirat sekhon
mob 0478162093
contact us for any refrigerator or dry goods delivery
deliver all over melbourne

```html
<!DOCTYPE html>
<html lang="en">
<head>
<meta charset="utf-8">
<title>Harvel Transport – Business Card</title>
<link href="https://fonts.googleapis.com/css2?family=Arimo:wght@400&display=swap" rel="stylesheet">
<style>
  :root {
    --brand-red: #952320;
    --card-white: #ffffff;
    --card-white-shade: #ececec;
    --page-bg: #f2efea;
    --ink-light: #ffffff;
    --shadow: rgba(0, 0, 0, 0.28);
  }
  * { margin: 0; padding: 0; box-sizing: border-box; }
  html, body {
    width: 1059px;
    height: 1200px;
    overflow: hidden;
  }
  body {
    position: relative;
    background: var(--page-bg);
    font-family: "Arimo", Arial, sans-serif;
  }
  .card {
    position: absolute;
    width: 364px;
    height: 588px;
    box-shadow: 3px 5px 8px var(--shadow);
    overflow: hidden;
  }
  .card p { position: absolute; line-height: 1; white-space: nowrap; }

  /* Front */
  .card-front {
    left: 101px;
    top: 91px;
    background: linear-gradient(to bottom, var(--card-white) 0%, var(--card-white-shade) 100%);
    color: var(--brand-red);
  }
  .side-bar {
    position: absolute;
    left: 0; top: 0;
    width: 25px;
    height: 100%;
    background: var(--brand-red);
  }
  .side-bar-gap {
    position: absolute;
    left: 0;
    width: 25px;
    height: 8px;
    background: var(--card-white);
  }
  .gap-one { top: 342px; }
  .gap-two { top: 416px; }
  .brand-mark {
    position: absolute;
    left: 111px;
    top: 110px;
    width: 150px;
    height: 150px;
  }
  .wordmark-main {
    left: 25px; right: 0;
    top: 300px;
    text-align: center;
    font-size: 62px;
    letter-spacing: 0.5px;
  }
  .wordmark-sub {
    left: 25px; right: 0;
    top: 386px;
    text-align: center;
    font-size: 45px;
    letter-spacing: 0.5px;
  }
  .contact-name {
    right: 28px;
    top: 499px;
    font-size: 20px;
    word-spacing: 3px;
  }
  .contact-phone {
    right: 28px;
    top: 532px;
    font-size: 15px;
    letter-spacing: 1px;
    word-spacing: 2px;
  }

  /* Back */
  .card-back {
    left: 576px;
    top: 567px;
    background: var(--brand-red);
    color: var(--ink-light);
  }
  .back-title {
    left: 0; right: 0;
    top: 72px;
    text-align: center;
    font-size: 20px;
    letter-spacing: 0.5px;
    word-spacing: 3px;
  }
  .service-list {
    position: absolute;
    left: 0; right: 0;
    top: 183px;
    text-align: center;
    font-size: 19px;
    line-height: 32px;
    word-spacing: 4px;
    list-style: none;
  }
  .price-promise {
    left: 0; right: 0;
    top: 350px;
    text-align: center;
    font-size: 20px;
    letter-spacing: 0.5px;
    word-spacing: 4px;
  }
  .card-back .contact-name { right: 27px; top: 472px; }
  .card-back .contact-phone { right: 27px; top: 502px; }
</style>
</head>
<body>
  <section class="card card-front" aria-label="Business card front">
    <div class="side-bar"></div>
    <div class="side-bar-gap gap-one"></div>
    <div class="side-bar-gap gap-two"></div>
    <svg class="brand-mark" viewBox="0 0 150 150" aria-hidden="true">
      <circle cx="75" cy="75" r="70" fill="var(--brand-red)"/>
    </svg>
    <p class="wordmark-main">HARVEL</p>
    <p class="wordmark-sub">TRANSPORT</p>
    <p class="contact-name">Mankirat Sekhon</p>
    <p class="contact-phone">mob 0478162093</p>
  </section>

  <section class="card card-back" aria-label="Business card back">
    <p class="back-title">HARVEL TRANSPORT</p>
    <ul class="service-list">
      <li>Contact Us</li>
      <li>For Any Refrigerator</li>
      <li>Or Dry Goods Delivery</li>
      <li>Deliver All Over Melbourne</li>
    </ul>
    <p class="price-promise">WE WILL BEAT ANY PRICE!</p>
    <p class="contact-name">Mankirat Sekhon</p>
    <p class="contact-phone">mob 0478162093</p>
  </section>
</body>
</html>
```